Email Signature - GILDED HARBOUR STAYS

Hi there,

I'm after an email signature for my email. I have attached a sample of what I like to this brief (File name: "Email Signature Sample").

I would like my email signature to have the following information:

Rosalind Vetterby
GILDED HARBOUR STAYS
Mobile: 0437 291 604 ( Australia )
Tel: +61 437 291 604 ( International )
Email: rosalind@gildedharbourstays.com
Website: www.gildedharbourstayscom

Industry/Entity Type

Online

Requirements
Must have
• I would like the signature to have a professional look

```html
<!DOCTYPE html>
<html lang="en">
<head>
<meta charset="UTF-8">
<title>Gilded Harbour Stays – Rosalind Vetterby</title>
<link rel="stylesheet" href="https://fonts.googleapis.com/css2?family=Ubuntu:wght@400;500&display=swap">
<style>
  :root {
    --navy: #16116b;
    --page: #e4e4e4;
    --card: #ffffff;
  }
  * { margin: 0; padding: 0; box-sizing: border-box; }
  html, body {
    width: 1200px;
    height: 734px;
    overflow: hidden;
    background: var(--page);
  }
  .card {
    position: absolute;
    left: 50px;
    top: 52px;
    width: 1100px;
    height: 630px;
    background: var(--card);
    color: var(--navy);
    font-family: "Ubuntu", sans-serif;
  }
  .card__divider {
    position: absolute;
    left: 0;
    top: 0;
    width: 1100px;
    height: 630px;
  }
  .card__name {
    position: absolute;
    left: 74px;
    top: 56px;
    font-size: 44px;
    font-weight: 400;
  }
  .brand {
    position: absolute;
    left: 536px;
    top: 110px;
    width: 540px;
    text-align: center;
  }
  .brand__dot {
    display: block;
    width: 96px;
    height: 96px;
    margin: 0 auto 34px;
    border-radius: 50%;
    background: var(--navy);
  }
  .brand__name {
    font-size: 36px;
    font-weight: 500;
    letter-spacing: 2px;
  }
  .contacts {
    position: absolute;
    left: 40px;
    top: 366px;
    list-style: none;
  }
  .contacts__item {
    display: flex;
    align-items: center;
    height: 49px;
    font-size: 26px;
  }
  .contacts__icon {
    width: 38px;
    height: 38px;
    margin-right: 20px;
    flex: none;
  }
</style>
</head>
<body>
  <main class="card">
    <svg class="card__divider" viewBox="0 0 1100 630" aria-hidden="true">
      <polygon points="8,118 888,620 880,620 8,122" fill="var(--navy)"/>
    </svg>

    <h1 class="card__name">Rosalind Vetterby</h1>

    <div class="brand">
      <span class="brand__dot"></span>
      <p class="brand__name">GILDED HARBOUR STAYS</p>
    </div>

    <ul class="contacts">
      <li class="contacts__item">
        <svg class="contacts__icon" viewBox="0 0 38 38" aria-hidden="true">
          <rect x="10" y="2" width="18" height="34" rx="3" fill="none" stroke="var(--navy)" stroke-width="2.5"/>
          <rect x="13" y="7" width="12" height="21" fill="var(--navy)"/>
          <circle cx="19" cy="32" r="1.6" fill="var(--navy)"/>
        </svg>
        0437 291 604 ( Australia )
      </li>
      <li class="contacts__item">
        <svg class="contacts__icon" viewBox="0 0 38 38" aria-hidden="true">
          <path d="M3 13 Q19 2 35 13 L35 17 L28 17 L27 12 L11 12 L10 17 L3 17 Z" fill="var(--navy)"/>
          <path d="M11 16 L27 16 L33 34 L5 34 Z" fill="var(--navy)"/>
          <circle cx="19" cy="25" r="4" fill="var(--card)"/>
        </svg>
        +61 437 291 604 ( International )
      </li>
      <li class="contacts__item">
        <svg class="contacts__icon" viewBox="0 0 38 38" aria-hidden="true">
          <circle cx="19" cy="19" r="16" fill="none" stroke="var(--navy)" stroke-width="2.5"/>
          <path d="M8 12 Q14 10 16 15 Q13 20 17 24 L14 31 Q7 26 6 18 Z" fill="var(--navy)"/>
          <path d="M22 6 Q28 9 32 15 Q26 17 24 13 Z" fill="var(--navy)"/>
        </svg>
        www.gildedharbourstays.com
      </li>
      <li class="contacts__item">
        <svg class="contacts__icon" viewBox="0 0 38 38" aria-hidden="true">
          <rect x="2" y="8" width="34" height="23" fill="var(--navy)"/>
          <path d="M4 10 L19 22 L34 10 M4 29 L15 19 M34 29 L23 19" fill="none" stroke="var(--card)" stroke-width="1.6"/>
        </svg>
        rosalind@gildedharbourstays.com
      </li>
      <li class="contacts__item">
        <svg class="contacts__icon" viewBox="0 0 38 38" aria-hidden="true">
          <circle cx="19" cy="19" r="13" fill="var(--navy)"/>
        </svg>
        rosalindvetterby ( Chat ID )
      </li>
    </ul>
  </main>
</body>
</html>
```